Financial Services General Marketing Brochure

Need a brochure to help recipients understand what makes BHC unique and the services that we offer. Must match look/feel of website https://brightharborcollective.com Layouts should make it easy to read the content - content should not be crammed into a traditional size/layout. Please see attached creative brief for specifics.

Target Market(s)

Financial advisors and mature couples looking for trustee services.

Industry/Entity Type

Financial Service

Colors
34a7d8
ffc214

Requirements
Must have
• See Creative Brief

```html
<!DOCTYPE html>
<html lang="en">
<head>
<meta charset="utf-8">
<title>BHC Brochure – Inside Spread</title>
<link href="https://fonts.googleapis.com/css2?family=Merriweather:ital,wght@0,300;0,400;1,700&family=Open+Sans:wght@400;600&display=swap" rel="stylesheet">
<style>
  :root{
    --slate:#557895;
    --cream:#f3ebe1;
    --circle-fill:#f7f1ea;
    --tan:#c9b49c;
    --gold:#e8a531;
    --ink:#555a60;
    --title:#52708c;
    --border:#c8c8c8;
    --fold:#9a9a9a;
  }
  *{margin:0;padding:0;box-sizing:border-box}
  html,body{width:1200px;height:1000px;overflow:hidden;background:#fff}
  .canvas{position:relative;width:1200px;height:1000px}
  .spread{position:absolute;left:0;top:200px;width:1200px;height:600px;border:1px solid var(--border);background:#fff}
  .fold-line{position:absolute;left:599px;top:180px;height:640px;border-left:1px dashed var(--fold)}

  /* left panel */
  .intro-panel{position:absolute;left:0;top:0;width:300px;height:600px;background:var(--slate)}
  .portrait{position:absolute;left:0;top:0;width:300px;height:166px;
    background:linear-gradient(120deg,#7d7468 0%,#b9aa95 45%,#3f5672 80%,#2c3e58 100%)}
  .intro-text{position:absolute;left:42px;top:202px;width:222px;color:#fff;
    font-family:"Merriweather",Georgia,serif;font-weight:300;font-size:11px;line-height:17.4px}
  .intro-text p{margin-bottom:17.4px}
  .drop-cap{float:left;font-size:38px;line-height:32px;font-weight:400;margin:3px 8px 0 0}
  .signature{position:absolute;left:94px;top:534px;color:#fff;font-family:"Open Sans",Arial,sans-serif;font-size:13px;line-height:18px}
  .signature strong{font-weight:600}

  /* middle panel */
  .unique-panel{position:absolute;left:300px;top:0;width:299px;height:600px}
  .unique-header{position:absolute;left:0;top:33px;width:299px;height:66px;background:var(--cream);
    display:flex;align-items:center;justify-content:center;
    font-family:"Merriweather",Georgia,serif;font-weight:400;font-size:17px;color:var(--title)}
  .qualities{position:absolute;left:25px;top:131px;width:260px}
  .quality h3{font-family:"Merriweather",Georgia,serif;font-style:italic;font-weight:700;font-size:14px;line-height:18px;color:var(--gold);margin-bottom:4px}
  .quality p{font-family:"Open Sans",Arial,sans-serif;font-size:10.5px;line-height:15px;color:var(--ink);white-space:nowrap;margin-bottom:16px}

  /* right panel */
  .team-panel{position:absolute;left:600px;top:0;width:599px;height:598px;
    background:linear-gradient(90deg,#ffffff 0%,#ffffff 55%,#fdf7ee 100%)}
  .team-header{position:absolute;left:0;top:33px;width:599px;height:66px;background:var(--slate);
    color:#fff;text-align:center;font-family:"Merriweather",Georgia,serif;font-weight:400;font-size:18px;line-height:26px;padding-top:7px}
  .team-diagram{position:absolute;left:0;top:0}
  .node-label{font-family:"Open Sans",Arial,sans-serif;font-size:18px;fill:var(--title)}
  .node-sub{font-family:"Open Sans",Arial,sans-serif;font-size:8px;fill:var(--ink)}
  .node-mid{font-family:"Open Sans",Arial,sans-serif;font-size:12.5px;fill:var(--title)}
</style>
</head>
<body>
<div class="canvas">
  <div class="spread">
    <section class="intro-panel">
      <div class="portrait" role="img" aria-label="Portrait photo of the founding principal in an office"></div>
      <div class="intro-text">
        <p><span class="drop-cap">I</span>f done well, a family’s transfer of wealth can be an incredible blessing, or if done improperly, can be terribly destructive. Often a neutral third party is needed to come alongside the family’s advisory team to provide guidance as families go through their wealth transition.</p>
        <p>Our relational focus, and Shared Compass approach, helps families to successfully navigate through the complexities of wealth, family and trusts. We believe a family “legacy” is about more than just money.</p>
      </div>
      <div class="signature"><strong>Daniel Ashford, J.D.</strong><br>Founding Principal</div>
    </section>

    <section class="unique-panel">
      <h2 class="unique-header">What Makes BHC Unique</h2>
      <div class="qualities">
        <div class="quality"><h3>Responsive</h3><p>The family deals directly with decision makers<br>instead of being subject to committees with<br>whom the family may never have the opportunity<br>to interact or engage.</p></div>
        <div class="quality"><h3>Family Focus</h3><p>We help families successfully navigate the<br>complexities of family wealth, not just perform<br>trust administration.</p></div>
        <div class="quality"><h3>Independent</h3><p>To avoid any conflicts of interest, we have no<br>formal affiliations with wealth management firms<br>or financial advisory practices.</p></div>
        <div class="quality"><h3>Customized</h3><p>Together we develop a customized approach that<br>will best suit the family's needs.</p></div>
        <div class="quality"><h3>Collaborative</h3><p>We work collaboratively with the family's team of<br>trusted professionals.</p></div>
      </div>
    </section>

    <section class="team-panel">
      <h2 class="team-header">Bright Harbor Collective<br>Client/Family Centered Team</h2>
      <svg class="team-diagram" width="599" height="598" viewBox="600 200 599 598">
        <g stroke="var(--tan)" stroke-width="3" fill="none">
          <line x1="746" y1="495" x2="808" y2="495"/>
          <line x1="992" y1="495" x2="1051" y2="495"/>
          <line x1="805" y1="625" x2="854" y2="577"/>
          <line x1="996" y1="625" x2="946" y2="577"/>
        </g>
        <g fill="var(--circle-fill)" stroke="var(--tan)" stroke-width="3">
          <circle cx="686" cy="495" r="60"/>
          <circle cx="1111" cy="495" r="60"/>
          <circle cx="763" cy="668" r="60"/>
          <circle cx="1038" cy="668" r="60"/>
          <circle cx="900" cy="712" r="60"/>
        </g>
        <g role="img" aria-label="Photo of a smiling adult woman">
          <circle cx="816" cy="372" r="59" fill="#e6d6c3" stroke="var(--tan)" stroke-width="3"/>
        </g>
        <g role="img" aria-label="Photo of two young grandchildren">
          <circle cx="985" cy="372" r="59" fill="#ece7e2" stroke="var(--tan)" stroke-width="3"/>
        </g>
        <g role="img" aria-label="Photo of a smiling senior couple">
          <polygon points="808,495 854,415 946,415 992,495 946,577 854,577" fill="#d9cfc6" stroke="var(--tan)" stroke-width="3"/>
        </g>
        <text class="node-label" x="686" y="502" text-anchor="middle">Attorney</text>
        <text class="node-label" x="1111" y="502" text-anchor="middle">Accountant</text>
        <text class="node-label" x="763" y="675" text-anchor="middle">Financial</text>
        <text class="node-label" x="1038" y="675" text-anchor="middle">Trustee</text>
        <text class="node-mid" x="900" y="691" text-anchor="middle">Human Capital</text>
        <text class="node-mid" x="900" y="706" text-anchor="middle">Resources</text>
        <text class="node-sub" x="900" y="724" text-anchor="middle">Legacy Development</text>
        <text class="node-sub" x="900" y="735" text-anchor="middle">Health Care Management</text>
        <text class="node-sub" x="900" y="746" text-anchor="middle">Philanthropic Services</text>
        <text class="node-sub" x="900" y="757" text-anchor="middle">Life Coaching</text>
      </svg>
    </section>
  </div>
  <div class="fold-line"></div>
</div>
</body>
</html>
```